Consumer and commercial IOT solutions (Internet Of Things)

We are a startup and are looking for business cards with logo. The logo will appear on all of our media as well as our ecommerce site and social sites that have yet to be developed. We want to present a fresh face on a high tech company that innovates at every turn. You can read about our solutions on our information only web site www.plorbaxsystems.net - We have some wording we would like used on our business cards but there is no place for this except for here. The company name is "Plorbax Systems" I have some samples of logos I am interested in seeing but I will let your team make the initial presentations

```html
<!DOCTYPE html>
<html lang="en">
<head>
<meta charset="UTF-8">
<title>Plorbax Systems — Business Card</title>
<link href="https://fonts.googleapis.com/css2?family=Belleza&display=swap" rel="stylesheet">
<style>
  :root {
    --backdrop: #2a2a2c;
    --brand-blue: #08a3e3;
    --brand-blue-deep: #0596d4;
    --card-white: #ffffff;
    --card-grey: #e6e6e7;
    --ink-dark: #3b3b3d;
    --ink-mid: #5a5a5c;
    --faint-white: rgba(255,255,255,0.16);
    --faint-grey: rgba(0,0,0,0.07);
  }
  * { box-sizing: border-box; margin: 0; padding: 0; }
  html, body { width: 1200px; height: 900px; overflow: hidden; }
  body {
    background: var(--backdrop);
    font-family: "Belleza", sans-serif;
    position: relative;
  }
  .card {
    position: absolute;
    left: 285px;
    width: 630px;
    height: 360px;
    overflow: hidden;
    box-shadow: 0 14px 30px rgba(0,0,0,0.5);
  }
  .card--front {
    top: 60px;
    background: linear-gradient(120deg, var(--brand-blue-deep), var(--brand-blue));
  }
  .card--back {
    top: 470px;
    background: linear-gradient(115deg, var(--card-grey) 0%, var(--card-white) 60%);
  }
  .decor-circle {
    position: absolute;
    border-radius: 50%;
  }
  .card--front .decor-circle {
    width: 460px; height: 460px;
    left: -40px; top: 110px;
    background: var(--faint-white);
  }
  .card--back .decor-circle {
    width: 480px; height: 480px;
    left: -40px; top: 50px;
    background: var(--faint-grey);
  }
  .brand {
    position: absolute;
    display: flex;
    flex-direction: column;
    align-items: center;
    gap: 18px;
  }
  .brand__dot {
    width: 72px; height: 72px;
    border-radius: 50%;
  }
  .brand__name {
    font-size: 30px;
    letter-spacing: 1.5px;
    white-space: nowrap;
  }
  .card--front .brand { left: 0; right: 0; top: 100px; }
  .card--front .brand__dot { background: var(--card-white); }
  .card--front .brand__name { color: var(--card-white); }
  .card--back .brand { right: 48px; top: 38px; }
  .card--back .brand__dot { background: var(--brand-blue); }
  .card--back .brand__name { color: var(--ink-dark); font-size: 32px; }
  .person {
    position: absolute;
    left: 48px; top: 150px;
  }
  .person__name {
    color: var(--brand-blue);
    font-size: 26px;
    letter-spacing: 0.5px;
  }
  .person__role {
    color: var(--ink-mid);
    font-size: 19px;
    margin-top: 2px;
  }
  .contact-list {
    position: absolute;
    left: 70px; top: 236px;
    list-style: none;
    color: var(--ink-mid);
    font-size: 16px;
  }
  .contact-list li {
    display: flex;
    align-items: center;
    gap: 10px;
    height: 24px;
  }
  .contact-list svg { width: 14px; height: 14px; fill: var(--brand-blue); }
  .divider {
    position: absolute;
    left: 60px; right: 130px; top: 314px;
    height: 1px;
    background: var(--brand-blue);
  }
  .address {
    position: absolute;
    left: 70px; top: 324px;
    display: flex;
    align-items: center;
    gap: 10px;
    color: var(--ink-mid);
    font-size: 16px;
  }
  .address svg { width: 12px; height: 16px; fill: var(--brand-blue); }
</style>
</head>
<body>

<section class="card card--front" aria-label="Business card front">
  <div class="decor-circle"></div>
  <div class="brand">
    <div class="brand__dot"></div>
    <div class="brand__name">PLORBAX SYSTEMS</div>
  </div>
</section>

<section class="card card--back" aria-label="Business card back">
  <div class="decor-circle"></div>
  <div class="brand">
    <div class="brand__dot"></div>
    <div class="brand__name">PLORBAX SYSTEMS</div>
  </div>

  <div class="person">
    <div class="person__name">DORIAN KESSEL</div>
    <div class="person__role">CO-FOUNDER &amp; CEO</div>
  </div>

  <ul class="contact-list">
    <li>
      <svg viewBox="0 0 24 24"><path d="M6.6 10.8a15 15 0 0 0 6.6 6.6l2.2-2.2a1 1 0 0 1 1-.25 11.4 11.4 0 0 0 3.6.57 1 1 0 0 1 1 1V20a1 1 0 0 1-1 1A17 17 0 0 1 3 4a1 1 0 0 1 1-1h3.5a1 1 0 0 1 1 1c0 1.25.2 2.45.57 3.57a1 1 0 0 1-.25 1z"/></svg>
      (555) 014-2290
    </li>
    <li>
      <svg viewBox="0 0 24 24"><path d="M12 2a10 10 0 1 0 0 20 10 10 0 0 0 0-20zm6.9 6h-2.9a15.7 15.7 0 0 0-1.4-3.6A8 8 0 0 1 18.9 8zM12 4c.8 1.2 1.5 2.5 1.9 4h-3.8c.4-1.5 1.1-2.8 1.900-4zM4.3 14a8 8 0 0 1 0-4h3.4a16 16 0 0 0 0 4zm.8 2h2.9c.3 1.3.8 2.500 1.4 3.6A8 8 0 0 1 5.1 16zM8 8H5.1a8 8 0 0 1 4.3-3.6C8.8 5.5 8.3 6.7 8 8zm4 12c-.8-1.2-1.5-2.5-1.9-4h3.8c-.4 1.5-1.1 2.8-1.9 4zm2.3-6H9.7a14.7 14.7 0 0 1 0-4h4.6a14.7 14.7 0 0 1 0 4zm.3 5.6c.6-1.1 1.1-2.3 1.4-3.6h2.9a8 8 0 0 1-4.3 3.6zm1.7-5.6a16 16 0 0 0 0-4h3.4a8 8 0 0 1 0 4z"/></svg>
      www.plorbaxsystems.net
    </li>
    <li>
      <svg viewBox="0 0 24 24"><path d="M2 5h20v14H2zm2 2v.5l8 5 8-5V7zm0 2.9V17h16V9.9l-8 5z"/></svg>
      dorian@plorbaxsystems.com
    </li>
  </ul>

  <div class="divider"></div>

  <div class="address">
    <svg viewBox="0 0 12 16"><path d="M6 0a6 6 0 0 0-6 6c0 4.5 6 10 6 10s6-5.5 6-10a6 6 0 0 0-6-6zm0 8.5A2.5 2.5 0 1 1 6 3.5a2.5 2.5 0 0 1 0 5z"/></svg>
    Maple Ridge, Illinois 60999, United States
  </div>
</section>

</body>
</html>
```